Boilerplate Management Organization Chart

"Our Management Approach is a deliberate step-by-step process and supports our Technical Approach detailed in proposal submission. The Management Approach covers all the human capital aspects for executing a contract—from contract award through to sustainment and/or transition of the contract to another company. It includes how we organize, hire, staff, train, and account for our contract employees—as well as their complete personal life-cycle management within the company."

We need this management approach to depict an amazing management process that demonstrates best practices of the project management body of knowledge. We need this vector image to be applicable to any proposal without making references to any other proposals. Generic names but using strong business language.
Updates

Thanks for all designs submitted thus far. Some have stuck to the original type of chart. We would like to see a completely different way to show the same information. It has to be able to be recognized and deciphered very quickly by people who might not necessarily want to look at it. It must draw them in and make it incredibly easy to distinguish a management approach that looks fresh, infallible, and easily implemented.

Target Market(s)

Federal space, Government organizations looking for procedural efficiencies,

Industry/Entity Type

Management

Requirements
Must have
• Must not take up more than 1/3 to 1/2 of printable page and be clear.
Should not have
• Not too much color, but should stick to some color palette of some interest.

```html
<!DOCTYPE html>
<html lang="en">
<head>
<meta charset="utf-8">
<title>Management Approach – Program Evaluation Cycle</title>
<link rel="stylesheet" href="https://fonts.googleapis.com/css2?family=Montserrat:wght@500;600;700&display=swap">
<style>
  :root {
    --navy: #05055f;
    --silver: #d6d6d6;
    --silver-edge: #c4c4c8;
    --divider: #7a7a7a;
    --badge-face: #ffffff;
    --badge-ink: #000000;
    --page: #ffffff;
  }
  html, body {
    margin: 0;
    padding: 0;
    width: 1200px;
    height: 1200px;
    overflow: hidden;
    background: var(--page);
  }
  .approach-wheel {
    display: block;
    width: 1200px;
    height: 1200px;
  }
  .wheel-disc { fill: var(--silver); }
  .banner-edge { fill: none; stroke: var(--silver-edge); stroke-width: 112; stroke-linecap: round; }
  .banner-band { fill: none; stroke: var(--navy); stroke-width: 100; stroke-linecap: round; }
  .banner-title {
    font-family: "Montserrat", sans-serif;
    font-weight: 700;
    font-size: 84px;
    fill: var(--silver);
    letter-spacing: 2px;
  }
  .divider { stroke: var(--divider); stroke-width: 1.5; }
  .phase-segment { fill: var(--navy); }
  .phase-label {
    font-family: "Montserrat", sans-serif;
    font-weight: 600;
    fill: var(--silver);
    text-anchor: middle;
  }
  .badge-ring { fill: url(#badgeRing); }
  .badge-face { fill: var(--badge-face); }
  .badge-number {
    font-family: "Montserrat", sans-serif;
    font-weight: 700;
    font-size: 40px;
    fill: var(--badge-ink);
    text-anchor: middle;
    dominant-baseline: central;
  }
</style>
</head>
<body>
<svg class="approach-wheel" viewBox="0 0 1500 1500" xmlns="http://www.w3.org/2000/svg">
  <defs>
    <radialGradient id="badgeRing" cx="50%" cy="40%" r="60%">
      <stop offset="0%" stop-color="#ffffff"/>
      <stop offset="70%" stop-color="#9a9a9a"/>
      <stop offset="100%" stop-color="#5a5a5a"/>
    </radialGradient>
    <path id="topTitlePath" d="M 230 438 A 605 605 0 0 1 1270 438"/>
    <path id="bottomTitlePath" d="M 222 1172 A 672 672 0 0 0 1278 1172"/>
  </defs>

  <!-- Base disc -->
  <circle class="wheel-disc" cx="750" cy="750" r="640"/>

  <!-- Title banners -->
  <g class="banner banner--top">
    <path class="banner-edge" d="M 201.5 420 A 640 640 0 0 1 1298.5 420"/>
    <path class="banner-band" d="M 201.5 420 A 640 640 0 0 1 1298.5 420"/>
    <text class="banner-title"><textPath href="#topTitlePath" startOffset="50%" text-anchor="middle" textLength="1170" lengthAdjust="spacing">MANAGEMENT APPROACH</textPath></text>
  </g>
  <g class="banner banner--bottom">
    <path class="banner-edge" d="M 250 1150 A 640 640 0 0 0 1250 1150"/>
    <path class="banner-band" d="M 250 1150 A 640 640 0 0 0 1250 1150"/>
    <text class="banner-title"><textPath href="#bottomTitlePath" startOffset="50%" text-anchor="middle" textLength="1060" lengthAdjust="spacing">PROGRAM EVALUATION</textPath></text>
  </g>

  <!-- Dividers -->
  <g class="dividers">
    <line class="divider" x1="750" y1="130" x2="750" y2="1340"/>
    <line class="divider" x1="225" y1="750" x2="1275" y2="750"/>
    <line class="divider" x1="315" y1="315" x2="1185" y2="1185"/>
    <line class="divider" x1="1185" y1="315" x2="315" y2="1185"/>
  </g>

  <!-- Phase segments (inner r 335, outer r 525) -->
  <g class="phase-segments">
    <path class="phase-segment" d="M 777.5 226.7 A 525 525 0 0 1 1094.4 353.8 L 969.8 497.2 A 335 335 0 0 0 767.5 415.5 Z"/>
    <path class="phase-segment" d="M 1146.2 405.6 A 525 525 0 0 1 1275 750 L 1085 750 A 335 335 0 0 0 1002.8 530.4 Z"/>
    <path class="phase-segment" d="M 1273.7 786.6 A 525 525 0 0 1 1140.1 1101.3 L 998.9 974.2 A 335 335 0 0 0 1084.2 773.4 Z"/>
    <path class="phase-segment" d="M 1094.4 1146.2 A 525 525 0 0 1 750 1275 L 750 1085 A 335 335 0 0 0 969.8 1002.8 Z"/>
    <path class="phase-segment" d="M 722.5 1274.3 A 525 525 0 0 1 405.6 1146.2 L 530.2 1002.8 A 335 335 0 0 0 732.5 1084.5 Z"/>
    <path class="phase-segment" d="M 342 1080.4 A 525 525 0 0 1 226.3 768.3 L 415.8 761.7 A 335 335 0 0 0 489.7 960.8 Z"/>
    <path class="phase-segment" d="M 226.3 704.2 A 525 525 0 0 1 359.8 398.7 L 501 525.8 A 335 335 0 0 0 415.8 721 Z"/>
    <path class="phase-segment" d="M 413.5 347.7 A 525 525 0 0 1 750 225 L 750 415 A 335 335 0 0 0 535.3 493.4 Z"/>
  </g>

  <!-- Phase labels -->
  <g class="phase-labels">
    <g transform="translate(955 352) rotate(22)">
      <text class="phase-label" font-size="30" x="0" y="0">Responsibility</text>
      <text class="phase-label" font-size="30" x="-8" y="36">Fixed</text>
    </g>
    <g transform="translate(1172 614) rotate(68)">
      <text class="phase-label" font-size="32" x="0" y="0">Management</text>
      <text class="phase-label" font-size="32" x="-4" y="36">&amp; Oversight</text>
    </g>
    <g transform="translate(1172 950) rotate(118)">
      <text class="phase-label" font-size="36" x="0" y="0">Manning</text>
      <text class="phase-label" font-size="32" x="10" y="38">the Team</text>
    </g>
    <g transform="translate(892 1162) rotate(163)">
      <text class="phase-label" font-size="38" x="0" y="0">Training</text>
    </g>
    <g transform="translate(548 1172) rotate(204)">
      <text class="phase-label" font-size="32" x="0" y="0">Professional</text>
      <text class="phase-label" font-size="32" x="8" y="36">Development</text>
    </g>
    <g transform="translate(333 880) rotate(-102)">
      <text class="phase-label" font-size="28" x="-28" y="0">Retention/</text>
      <text class="phase-label" font-size="28" x="0" y="32">Quality of Life</text>
    </g>
    <g transform="translate(352 565) rotate(-63)">
      <text class="phase-label" font-size="44" x="0" y="0">Benefits</text>
    </g>
    <g transform="translate(605 315) rotate(-20)">
      <text class="phase-label" font-size="32" x="0" y="0">Sustainment/</text>
      <text class="phase-label" font-size="32" x="8" y="38">Transition</text>
    </g>
  </g>

  <!-- Step badges -->
  <g class="step-badges">
    <g class="step-badge" transform="translate(790 320)">
      <circle class="badge-ring" r="38"/><circle class="badge-face" r="29"/>
      <text class="badge-number">1</text>
    </g>
    <g class="step-badge" transform="translate(1080 478) rotate(100)">
      <circle class="badge-ring" r="38"/><circle class="badge-face" r="29"/>
      <text class="badge-number">2</text>
    </g>
    <g class="step-badge" transform="translate(1178 790) rotate(90)">
      <circle class="badge-ring" r="38"/><circle class="badge-face" r="29"/>
      <text class="badge-number">3</text>
    </g>
    <g class="step-badge" transform="translate(1025 1080) rotate(140)">
      <circle class="badge-ring" r="38"/><circle class="badge-face" r="29"/>
      <text class="badge-number">4</text>
    </g>
    <g class="step-badge" transform="translate(708 1177) rotate(180)">
      <circle class="badge-ring" r="38"/><circle class="badge-face" r="29"/>
      <text class="badge-number">5</text>
    </g>
    <g class="step-badge" transform="translate(418 1022) rotate(200)">
      <circle class="badge-ring" r="38"/><circle class="badge-face" r="29"/>
      <text class="badge-number">6</text>
    </g>
    <g class="step-badge" transform="translate(322 708) rotate(270)">
      <circle class="badge-ring" r="38"/><circle class="badge-face" r="29"/>
      <text class="badge-number">7</text>
    </g>
    <g class="step-badge" transform="translate(475 418) rotate(300)">
      <circle class="badge-ring" r="38"/><circle class="badge-face" r="29"/>
      <text class="badge-number">8</text>
    </g>
  </g>
</svg>
</body>
</html>
```